Spa & Aesthetics business card design

Looking for business card designs for our spa. An excellent design would be able to be universally used by all employees - from staff to administrators to owners - and would be a simple but elegant depiction of a high end spa and aesthetics practice. We will be implementing a QR code on these cards, linked to our website. We are located in a desert setting so we would like to implement desert colors into our design (greens, hints of golds/beige, with a pop of color). We would also like to see some examples of embossed cards.
Should include:
Logo
First name, last name, credentials
Business address, phone number and email address
Space for QR code
Empty space on back to be able to hand write a short note or number as we hand out cards at events.
Please let me know if you need any additional info or formats of the design logo
high end cliental
see description

```html
<!DOCTYPE html>
<html lang="en">
<head>
<meta charset="utf-8">
<title>Solera Spa &amp; Aesthetics – Business Card</title>
<link href="https://fonts.googleapis.com/css2?family=Libre+Baskerville&family=Montserrat:wght@400&display=swap" rel="stylesheet">
<style>
  :root {
    --backdrop: #5c5c5e;
    --front-dark: #0e1412;
    --leaf-green: #2f4a30;
    --leaf-deep: #18261b;
    --cream: #f8ebd2;
    --cream-light: #faf0dd;
    --ink: #1d1915;
    --white: #ffffff;
  }
  * { margin: 0; padding: 0; box-sizing: border-box; }
  html, body { width: 900px; height: 1200px; overflow: hidden; }
  body {
    background: var(--backdrop);
    position: relative;
    font-family: "Montserrat", sans-serif;
  }
  .card {
    position: absolute;
    left: 188px;
    width: 525px;
    height: 298px;
    border-radius: 11px;
    overflow: hidden;
  }
  .card--front { top: 274px; background: var(--front-dark); }
  .card--back {
    top: 604px;
    background: linear-gradient(135deg, var(--cream-light), var(--cream));
  }
  .foliage {
    position: absolute; inset: 0;
    background:
      radial-gradient(ellipse 40% 35% at 20% 20%, var(--leaf-green), transparent 70%),
      radial-gradient(ellipse 35% 30% at 85% 25%, var(--leaf-green), transparent 70%),
      radial-gradient(ellipse 40% 35% at 55% 45%, var(--leaf-deep), transparent 75%),
      radial-gradient(ellipse 35% 30% at 85% 80%, var(--leaf-deep), transparent 70%),
      radial-gradient(ellipse 30% 30% at 10% 75%, var(--leaf-deep), transparent 70%),
      var(--front-dark);
  }
  .brand-name {
    font-family: "Libre Baskerville", serif;
    font-weight: 400;
    letter-spacing: 0.32em;
    white-space: nowrap;
    position: absolute;
  }
  .card--front .brand-name {
    color: var(--white);
    font-size: 38px;
    left: 0; right: 0;
    top: 124px;
    text-align: center;
    padding-left: 0.32em;
  }
  .card--back .brand-name {
    color: var(--ink);
    font-size: 26px;
    left: 30px; width: 220px;
    top: 134px;
    text-align: center;
    padding-left: 0.32em;
  }
  .divider {
    position: absolute;
    left: 262px; top: 80px;
    width: 1px; height: 138px;
    background: var(--ink);
  }
  .contact {
    position: absolute;
    left: 279px; top: 76px;
    color: var(--ink);
  }
  .contact__name {
    font-family: "Libre Baskerville", serif;
    font-size: 17px;
    letter-spacing: 0.02em;
    line-height: 22px;
  }
  .contact__role { font-size: 12px; letter-spacing: 0.05em; line-height: 18px; margin-bottom: 4px; }
  .contact__line { font-size: 12px; line-height: 21px; letter-spacing: 0.02em; }
  .contact__item {
    display: flex; align-items: center; gap: 6px;
    font-size: 12px; letter-spacing: 0.06em; line-height: 19px;
  }
  .contact__item:first-of-type { margin-top: 2px; }
  .icon { width: 9px; height: 9px; fill: var(--ink); flex: none; }
</style>
</head>
<body>
  <section class="card card--front">
    <div class="foliage" role="img" aria-label="Dark photograph of evergreen cypress branches"></div>
    <div class="brand-name">SOLERA</div>
  </section>

  <section class="card card--back">
    <div class="brand-name">SOLERA</div>
    <div class="divider"></div>
    <div class="contact">
      <p class="contact__name">MARIANNE L. HALE</p>
      <p class="contact__role">Founder + CEO</p>
      <p class="contact__line">1870 Palmetto Ave, Suite 3-204</p>
      <p class="contact__line">Coral Bay FL 34100</p>
      <p class="contact__item">
        <svg class="icon" viewBox="0 0 24 24"><path d="M6.6 10.8a15.1 15.1 0 0 0 6.6 6.6l2.2-2.2c.3-.3.7-.4 1-.2 1.1.4 2.3.6 3.6.6.6 0 1 .4 1 1V20c0 .6-.4 1-1 1A17 17 0 0 1 3 4c0-.6.4-1 1-1h3.5c.6 0 1 .4 1 1 0 1.3.2 2.5.6 3.6.1.3 0 .7-.2 1z"/></svg>
        555-014-2290
      </p>
      <p class="contact__item">
        <svg class="icon" viewBox="0 0 24 24"><path d="M2 5h20v14H2z M2 5l10 8 10-8" fill="var(--ink)" stroke="var(--cream)" stroke-width="1.5"/></svg>
        hello@solerastudio.com
      </p>
      <p class="contact__item">
        <svg class="icon" viewBox="0 0 24 24" fill="none" stroke="var(--ink)" stroke-width="2"><circle cx="12" cy="12" r="10"/><path d="M2 12h20M12 2c3 3 3 17 0 20M12 2c-3 3-3 17 0 20"/></svg>
        www.solerastudio.com
      </p>
    </div>
  </section>
</body>
</html>
```